Trendy eye catching business card for lawn mowing business

Verge Crew, a local community lawn mowing service, requires an eye catching trendy business card to drop into letterboxes.

We could simply throw something together from a Microsoft Word template, but we are wanting something more than this. Some other business’ images are attached for some inspiration.

We are requiring the card to have Verge Crew with our slogan, Call The Pellows. In addition, provide details with that we are a local, affordable lawn mowing service, and for other gardening matters to simply just ask!
Plus the relevant contact details, phone, email, social media.

Target Market(s)

Local community members who require assistance with their garden care

Industry/Entity Type

Gardening

Contact Information for Business Card

the name VERGE CREW is our logo
telephone logo 0493 218 067
email logo vergecrew@postbox-example.com
Instagram logo vergecrew
Facebook logo vergecrew.sth
Lawn Mowing Service
Local Affordable
edge trim, blow and clipping removal included.
Other gardening matters, just ask!

Font styles to use
Serif
Sans Serif
Decorative
Script

Colors
9bcb3c
ffffff

Requirements
Must have
• All the details listed in Business Card Details.
Make these words prominent:
Verge Crew
Lawn Mowing Service
Local
Affordable
Nice to have
• Our slogan ‘Call The Pellows’ incorporated.
Different colour background for front and reverse side
Greens, white and black colours
Subtle grass blades images incorporated
Should not have
• No images of lawnmowers.
No images of men/cartoons.
No using initials for Verge Crew

```html
<!DOCTYPE html>
<html lang="en">
<head>
<meta charset="utf-8">
<title>Verge Crew — Business Card</title>
<link href="https://fonts.googleapis.com/css2?family=Arimo:wght@400;700&family=Michroma&display=swap" rel="stylesheet">
<style>
  :root {
    --green: #84bd47;
    --green-deep: #74aa3c;
    --white: #ffffff;
    --ink: #141414;
    --grey: #6d6d6d;
    --backdrop: #3b3b3b;
  }
  * { margin: 0; padding: 0; box-sizing: border-box; }
  html, body {
    width: 1200px; height: 1015px; overflow: hidden;
    background: var(--backdrop);
    font-family: "Arimo", Arial, sans-serif;
  }
  .sheet {
    width: 1200px; height: 1015px;
    display: flex; flex-direction: column; align-items: center; justify-content: center;
    gap: 36px;
  }
  .card {
    position: relative; width: 820px; height: 469px; overflow: hidden;
    box-shadow: 0 10px 30px rgba(0,0,0,.45);
  }

  /* Front: green side */
  .card--front { background: var(--green); color: var(--white); }
  .card--front .grass-decor {
    position: absolute; left: 0; bottom: 0; width: 330px; height: 400px;
    background: linear-gradient(160deg, rgba(116,170,60,0) 20%, rgba(110,162,56,.75) 100%);
  }
  .front-copy {
    position: absolute; left: 250px; right: 40px; top: 120px; text-align: center;
  }
  .service-title { font-weight: 700; font-size: 40px; letter-spacing: 1.5px; line-height: 1.1; }
  .service-tagline { font-size: 31px; margin-top: 4px; }
  .service-details { font-size: 21px; line-height: 1.35; margin-top: 30px; }
  .service-phone { font-family: "Michroma", sans-serif; font-size: 34px; letter-spacing: 3px; margin-top: 10px; }

  /* Back: white side */
  .card--back { background: var(--white); color: var(--ink); }
  .card--back .base-band {
    position: absolute; left: 0; right: 0; bottom: 0; height: 22px; background: var(--green);
  }
  .card--back .grass-art {
    position: absolute; left: 0; bottom: 0; width: 300px; height: 330px;
    background: linear-gradient(175deg, rgba(132,189,71,.25) 0%, var(--green) 100%);
  }
  .brand {
    position: absolute; left: 330px; right: 40px; top: 70px; text-align: center;
  }
  .brand-name { font-weight: 700; font-size: 72px; letter-spacing: 1px; line-height: 1; color: var(--ink); }
  .brand-slogan {
    display: flex; align-items: center; gap: 14px; margin-top: 10px;
    color: var(--grey); font-weight: 700; font-size: 24px; letter-spacing: 5px;
  }
  .brand-slogan::before, .brand-slogan::after {
    content: ""; flex: 1; height: 1.5px; background: var(--grey);
  }
  .contacts {
    position: absolute; left: 360px; top: 250px; list-style: none;
    font-size: 21px; color: var(--ink);
  }
  .contacts li { display: flex; align-items: center; gap: 14px; height: 32px; }
  .contacts li.gap { margin-top: 18px; }
  .contacts svg { width: 24px; height: 24px; flex: none; }
  .social-dot { width: 22px; height: 22px; border-radius: 5px; background: var(--green); flex: none; }
</style>
</head>
<body>
<main class="sheet">

  <section class="card card--front" aria-label="Card front">
    <div class="grass-decor" role="img" aria-label="Faint grass blades rising from the lower left corner"></div>
    <div class="front-copy">
      <h1 class="service-title">LAWN MOWING SERVICE</h1>
      <p class="service-tagline">Local. Affordable.</p>
      <p class="service-details">Edge trim, blow and clipping removal included.<br>Other gardening matters, just ask!</p>
      <p class="service-phone">0493 218 067</p>
    </div>
  </section>

  <section class="card card--back" aria-label="Card back">
    <div class="grass-art" role="img" aria-label="Green grass blades illustration in the lower left corner"></div>
    <div class="base-band"></div>
    <div class="brand">
      <p class="brand-name">VERGE CREW</p>
      <p class="brand-slogan">CALL THE PELLOWS</p>
    </div>
    <ul class="contacts">
      <li>
        <svg viewBox="0 0 24 24" aria-hidden="true"><rect x="1" y="1" width="22" height="22" rx="4" fill="none" stroke="#84bd47" stroke-width="2"/><path d="M8 6l2 3-1.5 1.5a8 8 0 0 0 5 5L15 14l3 2-1 2.5c-6 0-11-5-11-11z" fill="#84bd47"/></svg>
        0493 218 067
      </li>
      <li>
        <svg viewBox="0 0 24 24" aria-hidden="true"><rect x="1" y="5" width="22" height="14" fill="#84bd47"/><path d="M1 5l11 8 11-8" fill="none" stroke="#fff" stroke-width="1.8"/></svg>
        vergecrew@postbox-example.com
      </li>
      <li class="gap"><span class="social-dot"></span>pics.example/vergecrew</li>
      <li><span class="social-dot"></span>social.example/vergecrew.sth</li>
    </ul>
  </section>

</main>
</body>
</html>
```